Northern Terrain Published Photographer Website

I need a website to feature a home page slide show of 6 of my top photos then a few simple pages including; gallery, bio, social, checkout, services
Updates

Need extra days to review

Target Market(s)

photography

Industry/Entity Type

Photographer

Coding

Coded - Design and coding required

Number of Pages Required

5+ page

Colors

Designer to choose colors to be used in the design.

Requirements
Must have
• clean eye catching elegant trendy
Nice to have
• unique and creative from other photographer websites

```html
<!DOCTYPE html>
<html lang="en">
<head>
<meta charset="utf-8">
<title>Northern Terrain — Photography</title>
<link href="https://fonts.googleapis.com/css2?family=Playfair+Display:wght@400;700;900&family=Montserrat:wght@400;500;600&family=Great+Vibes&display=swap" rel="stylesheet">
<style>
:root{
  --black:#000;
  --ink:#1f1f1f;
  --footer:#1b1b1b;
  --orange:#f7931e;
  --orange-deep:#ff7a00;
  --red:#ff3b0f;
  --paper:#f5f5f5;
  --muted:#8a8a8a;
  --faint:#ebebeb;
  --white:#fff;
}
*{margin:0;padding:0;box-sizing:border-box}
html,body{width:1200px;height:3178px;overflow:hidden}
body{position:relative;background:var(--white);font-family:"Montserrat",sans-serif;color:var(--ink)}
.abs{position:absolute}
.serif{font-family:"Playfair Display",serif}
.btn{position:absolute;background:var(--orange-deep);color:var(--white);border-radius:14px;font-size:11px;display:flex;align-items:center;justify-content:center}
.photo{position:absolute;border:2px solid var(--white);box-shadow:0 2px 6px rgba(0,0,0,.35)}

/* hero */
.hero{position:absolute;left:0;top:0;width:1200px;height:600px;background:var(--black)}
.hero-photo{position:absolute;left:260px;top:0;width:940px;height:600px;
  background:radial-gradient(ellipse at 78% 45%,#b8621c 0%,#6a3a16 22%,transparent 45%),
  linear-gradient(180deg,#2b2a22 0%,#3d3a2c 35%,#4a3a22 60%,#7a3f12 78%,#2a1a0d 100%)}
.brand{position:absolute;font-family:"Great Vibes",cursive;color:var(--white);font-size:26px}
.nav a{position:absolute;left:95px;color:var(--white);font-size:12px;text-decoration:none;font-weight:500}
.nav-mark{position:absolute;left:0;top:231px;width:107px;height:17px;background:var(--red)}
.dot-social{position:absolute;width:17px;height:17px;border-radius:50%;background:var(--white)}
.hero h1{position:absolute;left:292px;top:205px;color:var(--white);font-family:"Playfair Display",serif;font-weight:400;font-size:60px;letter-spacing:1px;line-height:1}
.hero .accent{position:absolute;left:464px;top:262px;color:var(--orange);font-family:"Playfair Display",serif;font-weight:900;font-size:76px;letter-spacing:2px;line-height:1}
.hero p{position:absolute;left:296px;top:360px;width:560px;color:#d8d2c6;font-size:11px;line-height:18px}
.rail{position:absolute;left:1085px;top:0;width:1px;height:600px;background:#cfcfcf}
.pager{position:absolute;left:1075px;width:20px;height:20px;border-radius:50%;background:#555;color:#bbb;font-size:11px;display:flex;align-items:center;justify-content:center}
.pager.on{background:var(--orange);color:var(--white)}
.about-line{position:absolute;top:545px;height:1px;background:#777}

/* bio */
.bio{position:absolute;left:0;top:600px;width:1200px;height:537px;background:var(--paper);overflow:hidden}
.ghost{position:absolute;font-family:"Playfair Display",serif;color:var(--faint);line-height:1;white-space:nowrap}
.bio h2{position:absolute;left:92px;top:148px;font-family:"Playfair Display",serif;font-size:50px;font-weight:700;color:var(--ink)}
.bio h3{position:absolute;left:92px;top:208px;font-size:34px;line-height:42px;font-weight:500;color:var(--ink)}
.bio p{position:absolute;left:94px;top:348px;width:500px;font-size:11px;line-height:18px;color:#555}

/* gallery */
.gallery{position:absolute;left:0;top:1137px;width:1200px;height:713px;overflow:hidden;background:var(--white)}
.gallery-bg{position:absolute;left:0;top:120px;width:1200px;height:593px;
  background:linear-gradient(180deg,#fff 0%,rgba(255,255,255,0) 30%),
  linear-gradient(90deg,#4a4d55 0%,#9aa0a8 25%,#c9ccd2 50%,#8d939c 75%,#3f434b 100%)}
.title-center{position:absolute;left:0;width:1200px;text-align:center;font-family:"Playfair Display",serif;font-weight:700;color:var(--ink)}

/* services */
.service h2{position:absolute;left:92px;top:1900px;font-family:"Playfair Display",serif;font-size:50px;font-weight:700;color:var(--ink)}
.service p.lead{position:absolute;left:95px;top:1976px;width:390px;font-size:11px;line-height:18px;color:var(--muted)}
.card{position:absolute;top:1946px;width:270px;height:157px;background:var(--white);box-shadow:0 2px 10px rgba(0,0,0,.1)}
.card h4{position:absolute;left:27px;top:47px;font-size:16px;font-weight:500;color:#333}
.card p{position:absolute;left:27px;top:78px;width:225px;font-size:11px;line-height:18.5px;color:var(--muted)}
.card-icon{position:absolute;top:-30px;left:38px;width:62px;height:62px;border-radius:50%;background:var(--white);box-shadow:0 2px 8px rgba(0,0,0,.12);display:flex;align-items:center;justify-content:center}

/* footer */
.footer{position:absolute;left:0;top:2923px;width:1200px;height:255px;background:var(--footer)}
.footer .txt{position:absolute;color:#9a9a9a;font-size:10px;line-height:18px}
.footer h5{position:absolute;color:var(--white);font-size:14px;font-weight:500}
.footer .link{position:absolute;left:464px;color:var(--white);font-size:10px}
</style>
</head>
<body>

<!-- HERO -->
<section class="hero">
  <div class="hero-photo" role="img" aria-label="Canyon butte glowing orange at dusk under a dark stormy sky"></div>
  <div class="brand" style="left:96px;top:14px">Northern Terrain</div>
  <div class="nav-mark"></div>
  <nav class="nav">
    <a style="top:232px">Home</a>
    <a style="top:270px">Bio</a>
    <a style="top:309px">Gallery</a>
    <a style="top:347px">Social</a>
    <a style="top:385px">Checkout</a>
    <a style="top:423px">Services</a>
  </nav>
  <span class="dot-social" style="left:94px;top:570px"></span>
  <span class="dot-social" style="left:122px;top:570px"></span>
  <span class="dot-social" style="left:150px;top:570px"></span>

  <h1>LOREM IPSUM</h1>
  <div class="accent">SIMPLE</div>
  <p>There are many variations of passages of Lorem Ipsum available, but the majority have suffered alteration in some form, by injected humour,believable.</p>
  <div class="btn" style="left:301px;top:438px;width:101px;height:26px">Learn More</div>

  <div class="rail"></div>
  <div class="pager on" style="top:259px">1</div>
  <div class="pager" style="top:291px">2</div>
  <div class="pager" style="top:323px">3</div>

  <div class="about-line" style="left:391px;width:232px"></div>
  <div class="about-line" style="left:728px;width:232px"></div>
  <div class="abs" style="left:623px;top:537px;width:105px;text-align:center;color:var(--white);font-size:14px;font-weight:500">About Us</div>
  <svg class="abs" style="left:666px;top:561px" width="14" height="16" viewBox="0 0 14 16"><path d="M7 1v13M2 9l5 5 5-5" fill="none" stroke="#f7931e" stroke-width="1.6"/></svg>
</section>

<!-- BIO -->
<section class="bio">
  <div class="ghost" style="left:84px;top:88px;font-size:110px">Bio</div>
  <h2>Bio</h2>
  <h3>Contrary to popular belief,<br>Lorem Ipsum is not simply<br>random text.</h3>
  <p>Marten Alder, a Latin professor &nbsp;at Larchmere College in Ontario, looked up one of the more obscure Latin words, consectetur, from a Lorem Ipsum passage.</p>
  <div class="btn" style="left:95px;top:410px;width:89px;height:23px">About Me</div>
  <div class="abs" style="left:692px;top:168px;width:412px;height:412px;border-radius:50%;background:#d9d9d9"></div>
  <div class="abs" role="img" aria-label="Young photographer in a mustard parka holding a camera" style="left:640px;top:30px;width:410px;height:507px;border-radius:180px 180px 0 0;background:linear-gradient(180deg,#6b4a32 0%,#c98a2e 45%,#b07020 75%,#3a2a1e 100%)"></div>
</section>

<!-- GALLERY -->
<section class="gallery">
  <div class="gallery-bg" role="img" aria-label="Snow-dusted forest along canyon walls"></div>
  <div class="ghost" style="left:0;width:1200px;text-align:center;top:braw;top:airline"></div>
  <div class="ghost" style="left:0;width:1200px;text-align:center;top:22px;font-size:98px">Our Gallery</div>
  <div class="title-center" style="top:70px;font-size:50px">Gallery</div>

  <div class="photo" role="img" aria-label="Heron silhouetted by old pier posts at golden sunset" style="left:137px;top:168px;width:386px;height:288px;background:linear-gradient(180deg,#c47a06 0%,#f0b020 35%,#d08a10 55%,#6a3c05 100%)"></div>
  <div class="photo" role="img" aria-label="River horseshoe bend through red canyon" style="left:536px;top:168px;width:250px;height:218px;background:radial-gradient(circle at 55% 55%,#2f6f5a 0%,#8a5a3a 35%,#a06a48 65%,#6e4a38 100%)"></div>
  <div class="photo" role="img" aria-label="Wide canyon vista under blue clouds" style="left:800px;top:168px;width:250px;height:218px;background:linear-gradient(180deg,#5f78a8 0%,#a9b4c8 35%,#8a8a8c 60%,#9c6a54 100%)"></div>
  <div class="photo" role="img" aria-label="Waterfall beneath an arched railway bridge in autumn woods" style="left:536px;top:402px;width:514px;height:276px;background:linear-gradient(90deg,#4e6a2a 0%,#a8a88a 40%,#dadad6 55%,#7a7a38 75%,#5a4a20 100%)"></div>
  <div class="photo" role="img" aria-label="Sunburst through a rock arch at dawn" style="left:138px;top:470px;width:186px;height:208px;background:linear-gradient(180deg,#2f66b8 0%,#7aa0d0 40%,#f0a040 60%,#8a5a3a 100%)"></div>
  <div class="photo" role="img" aria-label="Fiery clouds over snowy pines" style="left:338px;top:470px;width:186px;height:208px;background:linear-gradient(180deg,#f08a2a 0%,#e0502a 35%,#f0b060 60%,#7a7a80 85%,#d8d8dc 100%)"></div>
</section>

<!-- SERVICES -->
<section class="service">
  <h2>My Service</h2>
  <p class="lead">Lorem Ipsum has been the industry's standard dummy text ever since the 1500s, when an unknown printer took a galley of type and scrambled it to make a type specimen book. It has survived not only five centuries, but</p>
  <div class="btn" style="left:94px;top:2072px;width:95px;height:25px">Read More</div>

  <div class="card" style="left:534px">
    <div class="card-icon"><svg width="42" height="34" viewBox="0 0 42 34"><rect x="2" y="7" width="38" height="25" rx="4" fill="none" stroke="#333" stroke-width="2"/><path d="M13 7l3-5h10l3 5" fill="none" stroke="#333" stroke-width="2"/><circle cx="21" cy="19" r="8" fill="none" stroke="#333" stroke-width="2"/><circle cx="21" cy="19" r="4.5" fill="none" stroke="#333" stroke-width="1.5"/></svg></div>
    <h4>Lorem Ipsum</h4>
    <p>It is a long established fact that a reader will be distracted by the readable content of a page when looking at its</p>
  </div>
  <div class="card" style="left:835px">
    <div class="card-icon"><svg width="42" height="34" viewBox="0 0 42 34"><rect x="2" y="7" width="38" height="25" rx="4" fill="none" stroke="#333" stroke-width="2"/><path d="M13 7l3-5h10l3 5" fill="none" stroke="#333" stroke-width="2"/><circle cx="21" cy="19" r="8" fill="none" stroke="#333" stroke-width="2"/><circle cx="21" cy="19" r="4.5" fill="none" stroke="#333" stroke-width="1.5"/></svg></div>
    <h4>Lorem Ipsum</h4>
    <p>It is a long established fact that a reader will be distracted by the readable content of a page when looking at its</p>
  </div>
  <div class="abs" style="left:768px;top:2090px;width:28px;height:28px;border-radius:50%;border:4px solid var(--orange);background:var(--white)"></div>
  <div class="abs" style="left:534px;top:2123px;width:27px;height:3px;background:var(--orange)"></div>
  <div class="abs" style="left:565px;top:2123px;width:18px;height:3px;background:#888"></div>
  <div class="abs" style="left:588px;top:2123px;width:20px;height:3px;background:#888"></div>
</section>

<!-- INSTAGRAM -->
<section class="instagram">
  <div class="ghost" style="left:0;width:1200px;text-align:center;top:2180px;font-size:100px;color:#f2f2f2">Follow Us Instagram</div>
  <div class="title-center" style="top:2222px;font-size:52px">Follow Us Instagram</div>
  <div class="abs" role="img" aria-label="Bighorn sheep on red desert scrub" style="left:94px;top:2331px;width:203px;height:229px;background:linear-gradient(180deg,#8ab0d8 0%,#b49880 45%,#8a5a3a 100%)"></div>
  <div class="abs" role="img" aria-label="Glass sphere on a beach at violet dusk" style="left:297px;top:2331px;width:200px;height:229px;background:linear-gradient(180deg,#6a5ac8 0%,#c070a0 35%,#8a6ad8 60%,#3a3490 100%)"></div>
  <div class="abs" role="img" aria-label="Joshua tree silhouette against a pink sunset" style="left:497px;top:2316px;width:204px;height:259px;background:linear-gradient(180deg,#5a2a5a 0%,#c05060 40%,#7a3a4a 70%,#1a1018 100%)"></div>
  <div class="abs" role="img" aria-label="Canyon walls lit red under storm clouds" style="left:701px;top:2331px;width:202px;height:229px;background:linear-gradient(180deg,#2a2a48 0%,#5a4a6a 40%,#b04a2a 65%,#4a2a2a 100%)"></div>
  <div class="abs" role="img" aria-label="Snowy mountain range under pastel clouds" style="left:903px;top:2331px;width:203px;height:229px;background:linear-gradient(180deg,#6a6a9a 0%,#c890b0 35%,#8a8ab8 60%,#2a3060 100%)"></div>
</section>

<!-- NEWSLETTER -->
<section class="newsletter">
  <div class="abs" role="img" aria-label="Canyon rock formations at midday" style="left:0;top:2639px;width:1200px;height:300px;background:linear-gradient(180deg,#fff 0%,rgba(255,255,255,.6) 25%,rgba(255,255,255,0) 55%),linear-gradient(90deg,#6a5a4a 0%,#a89478 30%,#c4b49c 50%,#8a6a4a 75%,#4a3a2a 100%)"></div>
  <div class="title-center" style="top:2690px;font-size:52px">Newsletter Subscribe</div>
  <div class="abs" style="left:250px;top:2771px;width:685px;height:32px;background:#f2f2f2;color:#888;font-size:11px;padding:10px 36px">Email</div>
  <div class="btn" style="left:512px;top:2819px;width:175px;height:31px;border-radius:16px;font-size:19px">Subscribe</div>
  <svg class="abs" style="left:0;top:2900px" width="1200" height="30" viewBox="0 0 1200 30" preserveAspectRatio="none"><path d="M0 20 Q150 2 300 16 T600 14 T900 10 T1200 14 V30 H0Z" fill="#1b1b1b"/></svg>
</section>

<!-- FOOTER -->
<footer class="footer">
  <div class="brand" style="left:148px;top:54px;font-size:24px">Northern Terrain</div>
  <div class="txt" style="left:146px;top:103px;width:240px">There are many variations of passages of Lorem Ipsum available, but the majority have suffered alteration in some form, by injected humour</div>
  <span class="dot-social" style="left:146px;top:176px"></span>
  <span class="dot-social" style="left:174px;top:176px"></span>
  <span class="dot-social" style="left:202px;top:176px"></span>

  <span class="link" style="top:63px">Home</span>
  <span class="link" style="top:87px">Bio</span>
  <span class="link" style="top:111px">Gallery</span>
  <span class="link" style="top:135px">Social</span>
  <span class="link" style="top:159px">Checkout</span>
  <span class="link" style="top:183px">Services</span>

  <h5 style="left:627px;top:60px">Contact Us</h5>
  <svg class="abs" style="left:628px;top:99px" width="10" height="12" viewBox="0 0 10 12"><path d="M3 1 L1 3 Q2 8 7 11 L9 9 L7 7 L5.5 8 Q3.5 6.5 3 4.5 L4.5 3Z" fill="#fff"/></svg>
  <span class="txt" style="left:651px;top:96px;color:var(--white);letter-spacing:1px">555 (014)2287</span>
  <svg class="abs" style="left:624px;top:131px" width="14" height="10" viewBox="0 0 14 10"><rect x="1" y="1" width="12" height="8" fill="none" stroke="#fff"/><path d="M1 1l6 5 6-5" fill="none" stroke="#fff"/></svg>
  <span class="txt" style="left:651px;top:126px;color:var(--white)">hello@northernterrain.com</span>
  <svg class="abs" style="left:626px;top:156px" width="10" height="13" viewBox="0 0 10 13"><path d="M5 12 C1 7 1 5 1 4.5 A4 4 0 0 1 9 4.5 C9 5 9 7 5 12Z" fill="#fff"/><circle cx="5" cy="4.5" r="1.5" fill="#1b1b1b"/></svg>
  <span class="txt" style="left:651px;top:155px;color:var(--white)">Lorem Ipsum</span>

  <h5 style="left:851px;top:60px">Sing Up For Update</h5>
  <div class="abs" style="left:853px;top:101px;width:203px;height:25px;background:#2b2b2b;color:#555;font-size:10px;padding:6px 10px">Email</div>
  <div class="btn" style="left:853px;top:141px;width:84px;height:23px">Subscribe</div>
  <div class="txt" style="left:756px;top:181px;width:300px;text-align:right;font-size:9px;color:#777">© Copyright Northern Terrain 2019.All right Reserved</div>
</footer>

</body>
</html>
```